Farm product labels

This is meant to design a set of labels for the following products:
Sachets (similar to Brannigan’s ketchup):
- Size: W4xH9 cm. This is the internal area (inside the four sealing borders) of sachets. Front side contains the design, and back side just texts with the ingredients, nutrition facts and origin. Please check check the attached pictures related to sachet designs for your reference!
- Products:
o Ketchup
o Honey
o Nubakora (chocolate spread made of cacao, peanuts, and milk)
o Peanut butter
o Fruit jam (either Mango, Guava or Passion fruit)

Stickers (to be added on transparent bags):
- Size: W8xH14 cm. It does not need to be rectangular
- It needs to accommodate small texts with the ingredients, nutrition facts and origin
- Products:
o Tomato paste
o Fruit pulp (either Mango, Guava or Passion fruit)
o Processed vegetables (either Yuca or Sweet potato). They are peeled, chopped, pre-boiled and frozen.

For those interested I’ll provide detailed info as required

Target Market(s)

Hotels. The sachets are specially for breakfast

Requirements
Must have
• All product label designs should:
- Show a similar look, reflecting a single source/branding
- Be attractive and be easy to recognize each product
- Contain the logo of our farm (uploaded)

```html
<!DOCTYPE html>
<html lang="en">
<head>
<meta charset="utf-8">
<title>Kasoro Farm – Sachet Labels</title>
<link rel="stylesheet" href="https://fonts.googleapis.com/css2?family=Archivo+Black&family=Roboto+Condensed:wght@400;700&display=swap">
<style>
  :root {
    --ketchup: #e42a4c;
    --ketchup-deep: #c81b3b;
    --honey: #f7a928;
    --honey-deep: #f4c04a;
    --choco: #7a4636;
    --choco-deep: #5e3327;
    --peanut: #f47c22;
    --peanut-deep: #f9a45a;
    --passion: #bb74dc;
    --passion-deep: #9f55c4;
    --ink: #1d1d1d;
    --paper: #ffffff;
    --page: #ffffff;
  }
  * { box-sizing: border-box; margin: 0; padding: 0; }
  html, body { width: 1200px; height: 1022px; overflow: hidden; background: var(--page); }
  .sheet { position: relative; width: 1200px; height: 1022px; }
  .row { position: absolute; left: 9px; display: flex; gap: 28px; }
  .row--fronts { top: 22px; }
  .row--backs { top: 531px; }
  .label { position: relative; width: 214px; height: 484px; overflow: hidden; }
  .label--ketchup { background: var(--ketchup); --deep: var(--ketchup-deep); }
  .label--honey { background: var(--honey); --deep: var(--honey-deep); }
  .label--nubakora { background: var(--choco); --deep: var(--choco-deep); }
  .label--peanut { background: var(--peanut); --deep: var(--peanut-deep); }
  .label--passion { background: var(--passion); --deep: var(--passion-deep); }

  .artwork { position: absolute; inset: 0; width: 100%; height: 100%; }
  .artwork ellipse { fill: var(--deep); }

  .product-name {
    position: absolute; left: 28px; bottom: 80px;
    writing-mode: vertical-rl; transform: rotate(180deg);
    font-family: "Archivo Black", sans-serif; color: var(--paper);
    font-size: 66px; line-height: 0.92; letter-spacing: 1px;
    text-transform: uppercase; white-space: nowrap;
  }
  .product-name--two { font-size: 60px; left: 24px; }
  .product-name .variant {
    display: block; font-family: "Roboto Condensed", sans-serif; font-weight: 700;
    text-transform: none; font-size: 26px; letter-spacing: 0; line-height: 1.1;
  }
  .product-name--nubakora { font-size: 54px; bottom: 40px; }

  .farm-mark {
    position: absolute; left: 0; right: 0; bottom: 22px;
    display: flex; align-items: center; justify-content: center; gap: 6px;
    font-family: "Roboto Condensed", sans-serif; font-weight: 700;
    font-size: 13px; color: var(--paper);
  }
  .farm-mark::before {
    content: ""; width: 26px; height: 26px; border-radius: 50%; background: var(--paper);
  }
  .label--nubakora .farm-mark { top: 20px; bottom: auto; justify-content: flex-end; padding-right: 12px; }

  .nutrition {
    position: absolute; left: 15px; top: 56px; width: 186px; height: 414px;
    background: var(--paper); color: var(--ink); padding: 10px 10px 8px;
    font-family: "Roboto Condensed", sans-serif; font-size: 10px; line-height: 1.35;
  }
  .nutrition__title { font-family: "Roboto Condensed", sans-serif; font-weight: 700; font-size: 23px; line-height: 1.05; margin-bottom: 4px; }
  .nutrition__row { display: flex; justify-content: space-between; }
  .nutrition__row--indent { padding-left: 14px; }
  .nutrition__row--dv { justify-content: flex-end; font-size: 8px; margin: 2px 0 4px; }
  .nutrition b { font-weight: 700; }
  .nutrition__group { margin-top: 10px; }
  .nutrition__note { margin-top: 12px; font-size: 7px; line-height: 1.25; }
</style>
</head>
<body>
<main class="sheet">
  <section class="row row--fronts">
    <article class="label label--ketchup">
      <svg class="artwork" viewBox="0 0 214 484" role="img" aria-label="Tomato illustration"><ellipse cx="120" cy="150" rx="90" ry="110"/></svg>
      <h2 class="product-name">Ketchup</h2>
      <p class="farm-mark">Kasoro Farm</p>
    </article>
    <article class="label label--honey">
      <svg class="artwork" viewBox="0 0 214 484" role="img" aria-label="Honeycomb illustration"><ellipse cx="130" cy="230" rx="80" ry="150"/></svg>
      <h2 class="product-name">Honey</h2>
      <p class="farm-mark">Kasoro Farm</p>
    </article>
    <article class="label label--nubakora">
      <svg class="artwork" viewBox="0 0 214 484" role="img" aria-label="Cacao bean illustration"><ellipse cx="110" cy="200" rx="70" ry="80"/></svg>
      <h2 class="product-name product-name--nubakora">Nubakora<span class="variant">chocolate spread</span></h2>
      <p class="farm-mark">Kasoro Farm</p>
    </article>
    <article class="label label--peanut">
      <svg class="artwork" viewBox="0 0 214 484" role="img" aria-label="Peanut illustration"><ellipse cx="110" cy="190" rx="85" ry="150"/></svg>
      <h2 class="product-name product-name--two">Peanut<br>Butter</h2>
      <p class="farm-mark">Kasoro Farm</p>
    </article>
    <article class="label label--passion">
      <svg class="artwork" viewBox="0 0 214 484" role="img" aria-label="Passion fruit illustration"><ellipse cx="110" cy="140" rx="95" ry="105"/></svg>
      <h2 class="product-name product-name--two">Passion<br>Fruit<span class="variant">jam</span></h2>
      <p class="farm-mark">Kasoro Farm</p>
    </article>
  </section>

  <section class="row row--backs">
    <article class="label label--ketchup">
      <svg class="artwork" viewBox="0 0 214 484" role="img" aria-label="Tomato top illustration"><ellipse cx="107" cy="70" rx="95" ry="55"/></svg>
      <div class="nutrition">
        <h3 class="nutrition__title">Nutrition Facts</h3>
        <div class="nutrition__row"><b>Serving Size</b><span>...g</span></div>
        <div class="nutrition__row"><b>Servings Per Container</b><span></span></div>
        <div class="nutrition__group nutrition__row"><b>Amount Per Serving</b></div>
        <div class="nutrition__row"><b>Calories ...</b><span>Calories from Fat ...</span></div>
        <div class="nutrition__row nutrition__row--dv">% Daily Value*</div>
        <div class="nutrition__row"><b>Total Fat ...g</b><span>...%</span></div>
        <div class="nutrition__row nutrition__row--indent"><span>Saturated Fat ...g</span><span>...%</span></div>
        <div class="nutrition__row nutrition__row--indent"><span>Trans Fat ...g</span><span></span></div>
        <div class="nutrition__row"><b>Cholesterol ...mg</b><span>...%</span></div>
        <div class="nutrition__row"><b>Sodium ...mg</b><span>...%</span></div>
        <div class="nutrition__row"><b>Total Carbohydrate ...g</b><span>...%</span></div>
        <div class="nutrition__row nutrition__row--indent"><span>Dietary Fiber ...g</span><span>...%</span></div>
        <div class="nutrition__row nutrition__row--indent"><span>Sugars ...g</span><span></span></div>
        <div class="nutrition__row"><b>Protein ...g</b><span></span></div>
        <div class="nutrition__group nutrition__row"><span>Vitamin A</span><span>...%</span></div>
        <div class="nutrition__row"><span>Vitamin C</span><span>...%</span></div>
        <div class="nutrition__row"><span>Calcium</span><span>...%</span></div>
        <div class="nutrition__row"><span>Iron</span><span>...%</span></div>
        <p class="nutrition__note">* Percent Daily Values are based on a 2,000 calorie diet. Your daily values may be higher or lower depending on your calorie needs.</p>
      </div>
    </article>
    <article class="label label--honey">
      <svg class="artwork" viewBox="0 0 214 484" role="img" aria-label="Honeycomb top illustration"><ellipse cx="107" cy="60" rx="90" ry="50"/></svg>
      <div class="nutrition">
        <h3 class="nutrition__title">Nutrition Facts</h3>
        <div class="nutrition__row"><b>Serving Size</b><span>...g</span></div>
        <div class="nutrition__row"><b>Servings Per Container</b><span></span></div>
        <div class="nutrition__group nutrition__row"><b>Amount Per Serving</b></div>
        <div class="nutrition__row"><b>Calories ...</b><span>Calories from Fat ...</span></div>
        <div class="nutrition__row nutrition__row--dv">% Daily Value*</div>
        <div class="nutrition__row"><b>Total Fat ...g</b><span>...%</span></div>
        <div class="nutrition__row nutrition__row--indent"><span>Saturated Fat ...g</span><span>...%</span></div>
        <div class="nutrition__row nutrition__row--indent"><span>Trans Fat ...g</span><span></span></div>
        <div class="nutrition__row"><b>Cholesterol ...mg</b><span>...%</span></div>
        <div class="nutrition__row"><b>Sodium ...mg</b><span>...%</span></div>
        <div class="nutrition__row"><b>Total Carbohydrate ...g</b><span>...%</span></div>
        <div class="nutrition__row nutrition__row--indent"><span>Dietary Fiber ...g</span><span>...%</span></div>
        <div class="nutrition__row nutrition__row--indent"><span>Sugars ...g</span><span></span></div>
        <div class="nutrition__row"><b>Protein ...g</b><span></span></div>
        <div class="nutrition__group nutrition__row"><span>Vitamin A</span><span>...%</span></div>
        <div class="nutrition__row"><span>Vitamin C</span><span>...%</span></div>
        <div class="nutrition__row"><span>Calcium</span><span>...%</span></div>
        <div class="nutrition__row"><span>Iron</span><span>...%</span></div>
        <p class="nutrition__note">* Percent Daily Values are based on a 2,000 calorie diet. Your daily values may be higher or lower depending on your calorie needs.</p>
      </div>
    </article>
    <article class="label label--nubakora">
      <svg class="artwork" viewBox="0 0 214 484" role="img" aria-label="Cacao bean top illustration"><ellipse cx="107" cy="70" rx="70" ry="60"/></svg>
      <div class="nutrition">
        <h3 class="nutrition__title">Nutrition Facts</h3>
        <div class="nutrition__row"><b>Serving Size</b><span>...g</span></div>
        <div class="nutrition__row"><b>Servings Per Container</b><span></span></div>
        <div class="nutrition__group nutrition__row"><b>Amount Per Serving</b></div>
        <div class="nutrition__row"><b>Calories ...</b><span>Calories from Fat ...</span></div>
        <div class="nutrition__row nutrition__row--dv">% Daily Value*</div>
        <div class="nutrition__row"><b>Total Fat ...g</b><span>...%</span></div>
        <div class="nutrition__row nutrition__row--indent"><span>Saturated Fat ...g</span><span>...%</span></div>
        <div class="nutrition__row nutrition__row--indent"><span>Trans Fat ...g</span><span></span></div>
        <div class="nutrition__row"><b>Cholesterol ...mg</b><span>...%</span></div>
        <div class="nutrition__row"><b>Sodium ...mg</b><span>...%</span></div>
        <div class="nutrition__row"><b>Total Carbohydrate ...g</b><span>...%</span></div>
        <div class="nutrition__row nutrition__row--indent"><span>Dietary Fiber ...g</span><span>...%</span></div>
        <div class="nutrition__row nutrition__row--indent"><span>Sugars ...g</span><span></span></div>
        <div class="nutrition__row"><b>Protein ...g</b><span></span></div>
        <div class="nutrition__group nutrition__row"><span>Vitamin A</span><span>...%</span></div>
        <div class="nutrition__row"><span>Vitamin C</span><span>...%</span></div>
        <div class="nutrition__row"><span>Calcium</span><span>...%</span></div>
        <div class="nutrition__row"><span>Iron</span><span>...%</span></div>
        <p class="nutrition__note">* Percent Daily Values are based on a 2,000 calorie diet. Your daily values may be higher or lower depending on your calorie needs.</p>
      </div>
    </article>
    <article class="label label--peanut">
      <svg class="artwork" viewBox="0 0 214 484" role="img" aria-label="Peanut top illustration"><ellipse cx="107" cy="80" rx="95" ry="65"/></svg>
      <div class="nutrition">
        <h3 class="nutrition__title">Nutrition Facts</h3>
        <div class="nutrition__row"><b>Serving Size</b><span>...g</span></div>
        <div class="nutrition__row"><b>Servings Per Container</b><span></span></div>
        <div class="nutrition__group nutrition__row"><b>Amount Per Serving</b></div>
        <div class="nutrition__row"><b>Calories ...</b><span>Calories from Fat ...</span></div>
        <div class="nutrition__row nutrition__row--dv">% Daily Value*</div>
        <div class="nutrition__row"><b>Total Fat ...g</b><span>...%</span></div>
        <div class="nutrition__row nutrition__row--indent"><span>Saturated Fat ...g</span><span>...%</span></div>
        <div class="nutrition__row nutrition__row--indent"><span>Trans Fat ...g</span><span></span></div>
        <div class="nutrition__row"><b>Cholesterol ...mg</b><span>...%</span></div>
        <div class="nutrition__row"><b>Sodium ...mg</b><span>...%</span></div>
        <div class="nutrition__row"><b>Total Carbohydrate ...g</b><span>...%</span></div>
        <div class="nutrition__row nutrition__row--indent"><span>Dietary Fiber ...g</span><span>...%</span></div>
        <div class="nutrition__row nutrition__row--indent"><span>Sugars ...g</span><span></span></div>
        <div class="nutrition__row"><b>Protein ...g</b><span></span></div>
        <div class="nutrition__group nutrition__row"><span>Vitamin A</span><span>...%</span></div>
        <div class="nutrition__row"><span>Vitamin C</span><span>...%</span></div>
        <div class="nutrition__row"><span>Calcium</span><span>...%</span></div>
        <div class="nutrition__row"><span>Iron</span><span>...%</span></div>
        <p class="nutrition__note">* Percent Daily Values are based on a 2,000 calorie diet. Your daily values may be higher or lower depending on your calorie needs.</p>
      </div>
    </article>
    <article class="label label--passion">
      <svg class="artwork" viewBox="0 0 214 484" role="img" aria-label="Passion fruit top illustration"><ellipse cx="107" cy="70" rx="95" ry="55"/></svg>
      <div class="nutrition">
        <h3 class="nutrition__title">Nutrition Facts</h3>
        <div class="nutrition__row"><b>Serving Size</b><span>...g</span></div>
        <div class="nutrition__row"><b>Servings Per Container</b><span></span></div>
        <div class="nutrition__group nutrition__row"><b>Amount Per Serving</b></div>
        <div class="nutrition__row"><b>Calories ...</b><span>Calories from Fat ...</span></div>
        <div class="nutrition__row nutrition__row--dv">% Daily Value*</div>
        <div class="nutrition__row"><b>Total Fat ...g</b><span>...%</span></div>
        <div class="nutrition__row nutrition__row--indent"><span>Saturated Fat ...g</span><span>...%</span></div>
        <div class="nutrition__row nutrition__row--indent"><span>Trans Fat ...g</span><span></span></div>
        <div class="nutrition__row"><b>Cholesterol ...mg</b><span>...%</span></div>
        <div class="nutrition__row"><b>Sodium ...mg</b><span>...%</span></div>
        <div class="nutrition__row"><b>Total Carbohydrate ...g</b><span>...%</span></div>
        <div class="nutrition__row nutrition__row--indent"><span>Dietary Fiber ...g</span><span>...%</span></div>
        <div class="nutrition__row nutrition__row--indent"><span>Sugars ...g</span><span></span></div>
        <div class="nutrition__row"><b>Protein ...g</b><span></span></div>
        <div class="nutrition__group nutrition__row"><span>Vitamin A</span><span>...%</span></div>
        <div class="nutrition__row"><span>Vitamin C</span><span>...%</span></div>
        <div class="nutrition__row"><span>Calcium</span><span>...%</span></div>
        <div class="nutrition__row"><span>Iron</span><span>...%</span></div>
        <p class="nutrition__note">* Percent Daily Values are based on a 2,000 calorie diet. Your daily values may be higher or lower depending on your calorie needs.</p>
      </div>
    </article>
  </section>
</main>
</body>
</html>
```